Counseling Practice Business Card

I need a professional looking business card incorporating my new logo that was just completed. Card needs to incorporate my name and title, description of my specialty, my address, my phone number, my fax number, my email and my website URL. I need to be able to choose design on/with different paper colors and textures.
I do not have a lot of business card ideas so I am open to anything but I want bold,sharp, clear card without additional designs other than my logo (see attached file info). I am open to different color backgrounds or paper colors including black. I do not like traditional brackets around area codes in phone number or dashes between numbers in phone number. Am open to other ways of presenting including periods between numbers as appropriate. I do not know enough to know what I like yet but I want card to coordinate and work together with my logo. My practice emphasizes natural mental health interventions so any use of color (with background paper color or the blue and green in my logo) that elicits nature is nice. In addition to black, any natural brown or wood looking background might be desirable also. Most of the offerings so far look very similar and boring.

Target Market(s)

Potential therapy clients and other professionals

Contact Information for Business Card

Card information:
Marcus T. Whitfield, Ph.D.
Licensed Clinical Psychologist
Integrative Health Coach
4812 Ferndale Pkwy NW
Suite 730
Duluth, GA 30096
(770) 555-0142 phone
(770) 555-0186 fax
drmarcuswhitfield@kelvora.com
pathbloomcounseling.com

Font styles to use
Serif
Sans Serif
Other font styles liked:
• anything that you think looks crisp, clear and easily readable

Requirements
Must have
• Any color used should coordinate with my logo design (see attached files).
• Card should be printed horizontally so top and bottom are longest sides of rectangle.
• Background color or paper color should complement and highlight logo. Do not like a white background. black, grey, brown or any color my logo would blend well with.
Nice to have
• I would like designer to utilize color to highlight letters/name or phone-fax-web symbols.
• Bottom edge of card could be highlighted if appropriate to an idea.
Should not have
• I would NOT want the card to have a pure white background at all.
• No clear cards.
• Cards should be oriented with long sides on bottom and top, NOT sides. DO NOT LIKE THIS THIN TALL ORIENTATION.

```html
<!DOCTYPE html>
<html lang="en">
<head>
<meta charset="utf-8">
<title>Pathbloom Counseling – Business Card</title>
<link href="https://fonts.googleapis.com/css2?family=Roboto:wght@400;500;700&display=swap" rel="stylesheet">
<style>
  :root {
    --backdrop: #4b4c4f;
    --card: #1f2023;
    --ink-light: #e9eaec;
    --ink-muted: #c9cacd;
    --brand-blue: #2a7fc9;
    --brand-green: #1f7a3a;
    --foil: #6a6b6f;
  }
  * { box-sizing: border-box; margin: 0; padding: 0; }
  html, body {
    width: 799px; height: 1200px; overflow: hidden;
    background: var(--backdrop);
    font-family: "Roboto", Arial, sans-serif;
  }
  .card {
    position: absolute;
    left: 70px;
    width: 660px; height: 377px;
    background: var(--card);
    box-shadow: 0 18px 40px rgba(0,0,0,.45);
  }
  .card--front { top: 110px; }
  .card--back { top: 715px; }

  .brand {
    font-family: "Roboto", Arial, sans-serif;
    font-weight: 700;
    line-height: 1;
    white-space: nowrap;
  }
  .card--front .brand {
    position: absolute; left: 0; right: 0; top: 160px;
    text-align: center;
    font-size: 44px;
    color: var(--foil);
    letter-spacing: .5px;
  }

  .holder { position: absolute; left: 40px; top: 34px; }
  .holder__name { font-size: 22px; font-weight: 700; color: var(--brand-blue); }
  .holder__title { font-size: 11px; color: var(--ink-muted); margin-top: 4px; }

  .address {
    position: absolute; left: 40px; top: 120px;
    font-size: 14px; line-height: 1.35; color: var(--ink-light);
  }
  .contacts {
    position: absolute; left: 40px; top: 178px;
    list-style: none;
    font-size: 14px; line-height: 1; color: var(--ink-light);
  }
  .contacts li { display: flex; align-items: center; gap: 10px; height: 22px; }
  .contacts svg { width: 12px; height: 12px; fill: var(--brand-blue); flex: none; }

  .card--back .brand {
    position: absolute; right: 34px; bottom: 44px;
    font-size: 34px;
    color: var(--brand-blue);
  }

  .edge {
    position: absolute; left: 0; right: 0; bottom: 0; height: 7px;
    display: flex;
  }
  .edge__green { width: 46%; background: var(--brand-green); }
  .edge__blue { flex: 1; background: var(--brand-blue); }
</style>
</head>
<body>

<section class="card card--front">
  <p class="brand">Pathbloom Counseling</p>
</section>

<section class="card card--back">
  <div class="holder">
    <p class="holder__name">John Doe Smith</p>
    <p class="holder__title">Managing Director</p>
  </div>

  <p class="address">234 Anywhere St., Any City,<br>Any Town, US 123456</p>

  <ul class="contacts">
    <li>
      <svg viewBox="0 0 12 12" aria-hidden="true"><path d="M2.5 1h2l1 2.6-1.3 1a6.5 6.5 0 0 0 3.2 3.2l1-1.3L11 7.5v2A1.5 1.5 0 0 1 9.5 11 8.5 8.5 0 0 1 1 2.5 1.5 1.5 0 0 1 2.5 1z"/></svg>
      812.555.0140
    </li>
    <li>
      <svg viewBox="0 0 12 12" aria-hidden="true"><path d="M3 1h6v3H3zM1 5h10v5H9V8H3v2H1zM3.5 9h5v2h-5z"/></svg>
      812.555.0141
    </li>
    <li>
      <svg viewBox="0 0 12 12" aria-hidden="true"><path d="M1 2.5h10v7H1zM1.6 3.2 6 6.6l4.4-3.4" stroke="#1f2023" stroke-width=".9"/></svg>
      www.yourwebsite.com
    </li>
    <li>
      <svg viewBox="0 0 12 12" aria-hidden="true"><circle cx="6" cy="6" r="5"/><path d="M1 6h10M6 1c2 2.5 2 7.5 0 10M6 1c-2 2.5-2 7.5 0 10" stroke="#1f2023" stroke-width=".8" fill="none"/></svg>
      yourname@yourwebsite.com
    </li>
  </ul>

  <p class="brand">Pathbloom Counseling</p>

  <div class="edge">
    <span class="edge__green"></span>
    <span class="edge__blue"></span>
  </div>
</section>

</body>
</html>
```